Infografiken für Unternehmensberater
Zielgruppe
Unternehmensberater Zielgruppe Management Beratung ganzheitlich. Wie können Managerinnen noch erfolgreicher sein - durch und mit ihre Werte leben.
Aufgabenstellung
Ich habe den Prozess KORVELT ® registriert und möchte hierzu ein stimmiges Design das ich online verwenden kann und auch in meinen Präsentationen sowie als Kapitel Überschriften in meinem Buch zu dem Thema als auch auf meiner Homepage.
KORVELT® nach Halbig ist mein Management Prozess für erfolgreiche Managerinnen. Aus meiner 30jährigen Führungserfahrung.
DI - Dialog Aktives Zuhören, Dialogue Active Listening
N - Nenne und Erkenne das Problem: Name and Recognize the Problem
A - Anerkennung und Wertschätzung: Acknowledgement and Appreciation
M - Meine Stärken kennen und diese einsetzen je nach Situation: Know My Strengths and Apply Them According to the Situation
I - Intensives Handeln ins Tun kommen – machen: Intense Action into Doing – Execute
S - den Sinn kennen das warum als Grundlage des Prozesses: See and Knowing the Purpose, the Why as the Basis of the Process
Es muss nicht unbedingt in einem Kreis dargestellt werden - hier bin ich offen für gute Ideen.
Designelement können von der Homepage übernommen werden.

```html
<!DOCTYPE html>
<html lang="de">
<head>
<meta charset="utf-8">
<title>Der KORVELT Prozess nach Halbig</title>
<link href="https://fonts.googleapis.com/css2?family=Montserrat:wght@800&family=Poppins:wght@400;600;700&display=swap" rel="stylesheet">
<style>
  :root{
    --navy:#2c4580;
    --sky:#4bb0e4;
    --sky-pale:#d9eef9;
    --ring-grey:#dfe3ea;
    --ink:#2f3d5c;
    --text:#4a4f5c;
    --stage:#a3a3a3;
    --white:#ffffff;
  }
  *{margin:0;padding:0;box-sizing:border-box}
  html,body{width:1200px;height:1117px;overflow:hidden;background:var(--stage)}
  .poster{position:absolute;left:166px;top:66px;width:867px;height:984px;background:var(--white);
    box-shadow:6px 8px 14px rgba(0,0,0,.35);overflow:hidden;font-family:"Poppins",sans-serif}
  .poster svg.backdrop{position:absolute;left:0;top:0}
  .brand{position:absolute;top:20px;left:181px;width:492px;height:88px}
  .brand-mark{position:absolute;left:106px;top:18px;width:64px;height:64px;border:3px solid var(--navy);border-radius:50%}
  .brand-divider{position:absolute;left:197px;top:0;width:1px;height:78px;background:#c9ccd4}
  .brand-name{position:absolute;left:213px;top:16px;font-size:29px;font-weight:600;color:var(--ink);letter-spacing:.5px}
  .title{position:absolute;color:var(--white);font-family:"Montserrat",sans-serif;font-weight:800;line-height:1}
  .title-der{left:81px;top:113px;font-size:33px}
  .title-name{left:78px;top:148px;font-size:78px;letter-spacing:-1.5px}
  .title-side{left:490px;top:146px;font-size:36px;line-height:37px}
  .question{position:absolute;left:0;width:867px;top:232px;text-align:center;color:var(--white);font-size:37px;line-height:38px;font-weight:400}
  .question b{color:var(--sky);font-weight:600}
  .step-letter{position:absolute;width:70px;height:70px;margin:-35px 0 0 -35px;border-radius:50%;display:flex;align-items:center;justify-content:center;
    color:var(--white);font-family:"Montserrat",sans-serif;font-weight:800;font-size:36px;letter-spacing:-1px}
  .step-letter.light{background:var(--sky)}
  .step-letter.dark{background:var(--navy)}
  .step-visual{position:absolute;width:76px;height:76px;margin:-38px 0 0 -38px;border-radius:50%;
    background:radial-gradient(circle at 50% 45%,#ffffff 55%,#e8f0f7 100%);box-shadow:3px 5px 8px rgba(0,0,0,.15)}
  .step-visual.on-right{border:5px solid var(--ring-grey)}
  .step-visual.on-left{border:5px solid var(--sky-pale)}
  .step-text{position:absolute;font-size:13.5px;line-height:15px;color:var(--text)}
  .step-text h3{font-size:17.5px;line-height:19px;font-weight:700;color:var(--navy)}
  .step-text h3 + p{margin-bottom:5px}
  .step-text h3 span{color:var(--sky)}
  .step-text .en{margin-top:5px}
  .step-text .key{font-weight:700;font-size:17px;color:var(--sky)}
  .step-text .key .initial{color:var(--navy)}
  .step-text.left{left:119px}
  .step-text.right{left:589px}
  .url{position:absolute;left:0;width:867px;top:930px;text-align:center;color:var(--white);font-weight:700;font-size:19px}
</style>
</head>
<body>
<div class="poster">
  <svg class="backdrop" width="867" height="984" viewBox="0 0 867 984">
    <defs>
      <radialGradient id="glow" cx="0.8" cy="0.12" r="0.35">
        <stop offset="0" stop-color="#4bb0e4"/>
        <stop offset="1" stop-color="#2c4580" stop-opacity="0"/>
      </radialGradient>
      <linearGradient id="band" x1="0" y1="0" x2="0" y2="1">
        <stop offset="0" stop-color="#cfe9f7"/>
        <stop offset="1" stop-color="#ffffff" stop-opacity="0"/>
      </linearGradient>
      <path id="head" d="M0 19 L181 19 C205 19 220 30 235 50 L268 100 Q275 109 290 109 L560 109 Q572 109 580 100 L625 45 C645 22 660 19 680 19 L867 19 L867 247 L740 247 C715 247 705 255 690 275 L655 325 Q645 338 625 338 L240 338 Q222 338 212 325 L170 270 C158 254 150 247 130 247 L0 247 Z"/>
    </defs>
    <use href="#head" fill="#4bb0e4" transform="translate(0 9)"/>
    <use href="#head" fill="#2c4580"/>
    <use href="#head" fill="url(#glow)"/>

    <rect x="0" y="406" width="390" height="22" fill="url(#band)"/>
    <rect x="475" y="492" width="392" height="22" fill="url(#band)"/>
    <rect x="0" y="579" width="390" height="22" fill="url(#band)"/>
    <rect x="475" y="665" width="392" height="22" fill="url(#band)"/>
    <rect x="0" y="752" width="390" height="22" fill="url(#band)"/>
    <rect x="475" y="838" width="392" height="22" fill="url(#band)"/>

    <g stroke-width="3">
      <line x1="433" y1="406" x2="500" y2="406" stroke="#4bb0e4"/>
      <line x1="365" y1="492" x2="433" y2="492" stroke="#2c4580"/>
      <line x1="433" y1="579" x2="500" y2="579" stroke="#4bb0e4"/>
      <line x1="365" y1="665" x2="433" y2="665" stroke="#2c4580"/>
      <line x1="433" y1="752" x2="500" y2="752" stroke="#4bb0e4"/>
      <line x1="365" y1="838" x2="433" y2="838" stroke="#2c4580"/>
    </g>

    <rect x="0" y="951" width="867" height="15" fill="#2c4580"/>
    <rect x="0" y="972" width="867" height="12" fill="#4bb0e4"/>
    <path d="M228 984 L265 905 Q278 886 298 886 L568 886 Q588 886 601 905 L638 984 Z" fill="#ffffff"/>
    <path d="M236 984 L270 907 Q282 890 300 890 L566 890 Q584 890 596 907 L630 984 Z" fill="#4bb0e4"/>
  </svg>

  <div class="brand">
    <div class="brand-mark"></div>
    <div class="brand-divider"></div>
    <div class="brand-name">halbigjonas</div>
  </div>

  <div class="title title-der">DER</div>
  <div class="title title-name">KORVELT</div>
  <div class="title title-side">PROZESS<br>NACH HALBIG</div>
  <p class="question">Die <b>SINNFRAGE</b> Warum<br>machen wir es?</p>

  <div class="step-letter light" style="left:433px;top:406px">KO</div>
  <div class="step-visual on-right" style="left:535px;top:406px" role="img" aria-label="Linienzeichnung: zwei Personen im Gespräch"></div>
  <div class="step-text right" style="top:372px">
    <h3><span>KO</span>MMUNIKATION</h3><p>Aktives Zuhören</p>
    <h3><span>KO</span>NVERSATION</h3><p>active listening</p>
  </div>

  <div class="step-letter dark" style="left:433px;top:492px">R</div>
  <div class="step-visual on-left" style="left:331px;top:492px" role="img" aria-label="Linienzeichnung: nachdenkende Person"></div>
  <div class="step-text left" style="top:470px">
    <p><span class="key"><span class="initial">R</span>ICHTIG</span> benennen<br>und das Problem erkennen</p>
    <p class="en"><span class="key"><span class="initial">R</span>ECOGNIZE</span> and Name<br>the Problem</p>
  </div>

  <div class="step-letter light" style="left:433px;top:579px">V</div>
  <div class="step-visual on-right" style="left:535px;top:579px" role="img" aria-label="Linienzeichnung: Hände halten eine Kugel"></div>
  <div class="step-text right" style="top:545px">
    <h3><span>V</span>ERTRAUEN</h3><p>und Wertschätzung</p>
    <h3><span>V</span>ALIDATION</h3><p>and Appreciation</p>
  </div>

  <div class="step-letter dark" style="left:433px;top:665px">E</div>
  <div class="step-visual on-left" style="left:331px;top:665px" role="img" aria-label="Linienzeichnung: Person mit Gedankenblasen"></div>
  <div class="step-text left" style="top:620px">
    <p><span class="key"><span class="initial">E</span>IGENE</span> Stärken kennen<br>und diese einsetzen<br>je nach Situation</p>
    <p class="en"><span class="key"><span class="initial">E</span>MPLOY</span> My Strengths<br>and Apply Them According<br>to the Situation</p>
  </div>

  <div class="step-letter light" style="left:433px;top:752px">L</div>
  <div class="step-visual on-right" style="left:535px;top:752px" role="img" aria-label="Linienzeichnung: Bogenschütze zielt"></div>
  <div class="step-text right" style="top:706px">
    <h3><span>L</span>OSLEGEN</h3><p>Handeln ins Tun kommen<br>– machen</p>
    <h3><span>L</span>AUNCH</h3><p>Action into Doing Execute</p>
  </div>

  <div class="step-letter dark" style="left:433px;top:838px">T</div>
  <div class="step-visual on-left" style="left:331px;top:838px" role="img" aria-label="Linienzeichnung: Person mit Herz"></div>
  <div class="step-text left" style="top:780px">
    <p>Den <span class="key"><span class="initial">T</span>IEFEN</span> Sinn kennen,<br>das Warum als Grundlage<br>des Prozesses</p>
    <p class="en"><span class="key"><span class="initial">T</span>RUE</span> Purpose: Knowing<br>the Why as the Basis<br>of the Process</p>
  </div>

  <div class="url">www.halbigjonas.com</div>
</div>
</body>
</html>
```